BRIGHTVALE ADVISERS POWERPOINT PRESENTATION TEMPLATE 1

We need the ultimate quality Powerpoint presentation design.
We are the advisory firm working with modern world class tech companies throughout Europe, their founders, shareholders, and potential investors.
The new template must contain elements such as our logo, appropriate backgrounds, be at the same time very attractive visually and easy to rear. Also there must be some place where logo of our clients should be placed.

We like:
- icons and
- infographics,
so attractive design in this area will be greatly appreciated.

Please avoid serif fonts and excessive decorations such as "waves" or other similar decor.

We are also in contact with serious investors - wealthy individuals, reputable financial institutions, and their advisers; banks, private equity investors, global technology companies.

The Powerpoint template design must send a message that:
- we are a high technology oriented team of professionals,
- we provide modern financial advisory services
- but at the same time we are open minded, creative, yet very competent in the area of corporate finance.

The Powerpoint template must complement our business card design, first impression of a team of top notch professionals who advise top notch tech companies on their top notch corporate finance and M&A projects.

Enclosed are sets of our logo, current template, business card project which won previous competition.

It is perhaps a good basis to start with and get us to the template of our dreams.

While working on this project please think about the following firms which at some point may be looking at your design:
- Quorlin
- Tavindex
- Pelorim
- Veskaran (Zundle)
- Marowisp
- Turnequo
- Dovrash
- Kelvaro
- Obrethy

The quality of the design, its style, aesthetics must meet the top criteria in contemporary design trends.

Target Market(s)

Banks, financial investors, strategic investors

Industry/Entity Type

Finance

Font styles to use
Sans Serif

Requirements
Must have
• Icons
Infographics
Attractive backgrounds
Clean design
Harmonize with logo and emblem colors.
Should not have
• Excessive tacky decor (waves, etc)
Serif fonts
Excessive colors

```html
<!DOCTYPE html>
<html lang="en">
<head>
<meta charset="utf-8">
<title>Brightvale Advisers – Presentation Template</title>
<link href="https://fonts.googleapis.com/css2?family=Montserrat:wght@300;400;600;700;800&family=Open+Sans:wght@400;600;700&display=swap" rel="stylesheet">
<style>
:root{
  --stage:#e4e5e7;
  --paper:#f6f7f9;
  --ink:#1b2a4a;
  --navy:#1d3c86;
  --blue:#1f64bd;
  --bright:#2b7fd6;
  --sky:#9dbde6;
  --slate:#8c9db4;
  --line:#d3dbe6;
  --text:#3a4556;
}
*{box-sizing:border-box;margin:0;padding:0}
html,body{width:943px;height:1200px;overflow:hidden;background:var(--stage)}
body{position:relative;font-family:"Open Sans",Arial,sans-serif;color:var(--text)}
.slide{position:absolute;width:516px;height:290px;transform-origin:0 0;transform:scale(.5525);background:var(--paper);overflow:hidden;box-shadow:0 14px 26px rgba(0,0,0,.28)}
.slide.big{transform:scale(.593)}
.abs{position:absolute}
.title{position:absolute;left:20px;top:11px;font:800 12.5px "Montserrat",sans-serif;color:var(--ink)}
.sub{position:absolute;left:20px;top:25px;font:italic 400 5.5px "Open Sans",sans-serif;letter-spacing:3px;color:var(--sky);text-transform:uppercase}
.logo{position:absolute;right:16px;top:14px;display:flex;align-items:center;gap:3px;font:400 8.5px "Montserrat",sans-serif;color:var(--ink)}
.logo i{display:block;width:9px;height:9px;border:1.8px solid var(--blue);border-radius:50%}
.rule{position:absolute;left:20px;top:36px;width:24px;height:1.5px;background:var(--blue)}
.ft{position:absolute;left:0;right:0;bottom:0;height:18px;display:flex;font:600 4.5px "Montserrat",sans-serif;color:#fff}
.ft .n{width:26px;background:var(--navy);display:flex;align-items:center;justify-content:center;font-size:5.5px}
.ft .c{flex:1;background:linear-gradient(90deg,#1f5fb5,#2464bf);display:flex;align-items:center;justify-content:center;letter-spacing:2.5px}
.ft .l{width:78px;background:var(--slate);display:flex;align-items:center;justify-content:center;font-weight:400}
.lab{position:absolute;font:700 4.6px "Montserrat",sans-serif;color:var(--blue);text-transform:uppercase;border-bottom:1px solid var(--line);padding-bottom:2px}
.tag{position:absolute;background:var(--blue);color:#fff;font:600 4.2px "Open Sans",sans-serif;display:flex;align-items:center;justify-content:center;text-align:center;border-radius:1px}
.field{position:absolute;background:#fff;font:400 4.2px "Open Sans",sans-serif;color:var(--text);display:flex;align-items:center;padding-left:5px;box-shadow:0 1px 2px rgba(0,0,0,.08)}
.list{position:absolute;font:400 4px/1.6 "Open Sans",sans-serif;color:var(--text);list-style:none}
.list li::before{content:"✓ ";color:var(--blue)}
.dots li::before{content:"• "}
.card{position:absolute;background:#fff;box-shadow:0 1px 4px rgba(0,0,0,.12)}
.pill{position:absolute;background:var(--navy);color:#fff;border-radius:8px;font:600 4.6px "Open Sans",sans-serif;display:flex;align-items:center;justify-content:center}
table.grid{position:absolute;border-collapse:collapse;font:400 4.3px "Open Sans",sans-serif;color:var(--text)}
table.grid th{background:var(--blue);color:#fff;font-weight:700;text-align:right;padding:1.5px 4px}
table.grid th:first-child,table.grid td:first-child{text-align:left;color:var(--blue);font-weight:700}
table.grid td{text-align:right;padding:1.9px 4px;border-bottom:.5px solid var(--line)}
table.grid tr.b td{font-weight:700}
.stat{position:absolute;background:var(--navy);color:#fff;border-radius:5px;box-shadow:0 2px 5px rgba(0,0,0,.25)}
.stat.mid{background:var(--blue)}
.stat p{position:absolute;left:10px;top:8px;width:88px;font:700 3.9px/1.35 "Montserrat",sans-serif;text-transform:uppercase}
.stat b{position:absolute;right:10px;bottom:4px;font:700 27px "Montserrat",sans-serif}
.mapfill{position:absolute;border-radius:4px}
.svgabs{position:absolute;left:0;top:0}
</style>
</head>
<body>

<!-- 1 Cover -->
<section class="slide" style="left:22px;top:21px;background:linear-gradient(135deg,#2671c9,#1e4d9e)">
  <div class="abs" style="left:48px;top:30px;width:18px;height:18px;border:3px solid #fff;border-radius:50%;opacity:.9;left:52px"></div>
  <div class="abs" style="left:22px;top:56px;font:300 19px 'Montserrat',sans-serif;color:#fff;letter-spacing:.5px">BRIGHTVALE</div>
  <div class="abs" style="left:24px;top:93px;font:300 8px/1.35 'Montserrat',sans-serif;color:#fff">[BRIEF DESCRIPTION OF THE<br>COMPANY.<br><b style="font-weight:800">ONE-TWO SENTENCES</b>]</div>
  <div class="abs" style="left:24px;top:143px;font:400 5px 'Montserrat',sans-serif;color:#fff">[MONTH,YEAR]</div>
</section>

<!-- 2 Table of contents -->
<section class="slide" style="left:333px;top:21px">
  <div class="logo" style="left:62px;right:auto;top:82px"><i></i>BRIGHTVALE</div>
  <div class="abs" style="left:80px;top:92px;font:800 72px/1 'Montserrat',sans-serif;color:var(--ink)">1</div>
  <div class="abs" style="left:64px;top:170px;font:300 10px/1.2 'Montserrat',sans-serif;color:var(--ink)">TABLE OF<br><b style="font-weight:800">CONTENTS</b></div>
  <div class="abs" style="left:236px;top:10px;font:700 4px 'Montserrat',sans-serif;color:var(--blue)">I&nbsp; Introduction</div>
  <div class="abs" style="left:327px;top:10px;font:700 4px 'Montserrat',sans-serif;color:var(--slate)">II&nbsp; Company operations</div>
  <div class="abs" style="left:418px;top:10px;font:700 4px 'Montserrat',sans-serif;color:var(--slate)">III&nbsp; Market and competition</div>
  <div class="card" style="left:236px;top:28px;width:80px;height:112px;background:var(--blue);border-radius:4px"><ol class="list" style="left:6px;top:6px;color:#fff;list-style:decimal inside;font-size:3.4px"><li>Introduction</li><li>Basic information</li><li>Business development</li><li>Development plans</li><li>Investment thesis</li></ol></div>
  <div class="card" style="left:327px;top:28px;width:80px;height:112px;background:var(--slate);border-radius:4px"><ol class="list" style="left:6px;top:6px;color:#fff;list-style:decimal inside;font-size:3.4px"><li>Product portfolio</li><li>Product description</li><li>Production sites</li><li>Licenses</li><li>Business model</li><li>Marketing strategy</li><li>Customer groups</li><li>Sales structure</li><li>Key suppliers</li><li>Raw materials</li><li>Key people</li></ol></div>
  <div class="card" style="left:418px;top:28px;width:80px;height:112px;background:var(--slate);border-radius:4px"><ol class="list" style="left:6px;top:6px;color:#fff;list-style:decimal inside;font-size:3.4px"><li>Market overview</li><li>Market competition</li><li>Competitive edge</li></ol></div>
  <div class="abs" style="left:236px;top:149px;font:700 4px 'Montserrat',sans-serif;color:var(--slate)">IV&nbsp; Strategy and plans</div>
  <div class="abs" style="left:327px;top:149px;font:700 4px 'Montserrat',sans-serif;color:var(--slate)">V&nbsp; Financial information</div>
  <div class="abs" style="left:418px;top:149px;font:700 4px 'Montserrat',sans-serif;color:var(--slate)">VI&nbsp; Attachments</div>
  <div class="card" style="left:236px;top:163px;width:80px;height:104px;background:var(--slate);border-radius:4px"><ol class="list" style="left:6px;top:6px;color:#fff;list-style:decimal inside;font-size:3.4px"><li>Strategy plan</li><li>Acquisitions</li><li>Value proposition</li><li>SWOT analysis</li><li>Capex effects</li></ol></div>
  <div class="card" style="left:327px;top:163px;width:80px;height:104px;background:var(--slate);border-radius:4px"><ol class="list" style="left:6px;top:6px;color:#fff;list-style:decimal inside;font-size:3.4px"><li>Income statement</li><li>Revenue structure</li><li>Operating costs</li><li>Cost of goods</li><li>Sales profitability</li><li>Cash flow</li><li>Planned capex</li><li>Balance sheet</li></ol></div>
  <div class="card" style="left:418px;top:163px;width:80px;height:104px;background:var(--slate);border-radius:4px"><ol class="list" style="left:6px;top:6px;color:#fff;list-style:decimal inside;font-size:3.4px"><li>Financial statements</li><li>Glossary</li></ol></div>
  <div class="ft"><div class="n">3</div><div class="c">STRICTLY CONFIDENTIAL</div><div class="l">[Company logo]</div></div>
</section>

<!-- 3 Introduction -->
<section class="slide" style="left:641px;top:21px">
  <div class="title">INTRODUCTION</div><div class="sub">[Brief description of the company's activities]</div><div class="rule"></div>
  <div class="logo"><i></i>BRIGHTVALE</div>
  <div class="lab" style="left:20px;top:48px;width:226px">Basic information</div>
  <div class="tag" style="left:20px;top:58px;width:42px;height:12px">Headquarters</div><div class="field" style="left:66px;top:58px;width:180px;height:12px">[address]</div>
  <div class="tag" style="left:20px;top:74px;width:42px;height:12px">Industry</div><div class="field" style="left:66px;top:74px;width:180px;height:12px">[name of the industry]</div>
  <div class="tag" style="left:20px;top:90px;width:42px;height:12px">Headcount</div><div class="field" style="left:66px;top:90px;width:180px;height:12px">[number of employees]</div>
  <div class="tag" style="left:20px;top:106px;width:42px;height:18px">Ownership structure</div><div class="field" style="left:66px;top:106px;width:180px;height:18px">25.00%&nbsp;&nbsp;
    <svg width="12" height="12" viewBox="0 0 12 12"><circle cx="6" cy="6" r="4.5" fill="none" stroke="#d3dbe6" stroke-width="2"/><circle cx="6" cy="6" r="4.5" fill="none" stroke="#1d3c86" stroke-width="2" stroke-dasharray="14 30"/></svg>&nbsp;50.00%&nbsp;&nbsp;• Shareholder 1, 2, 3</div>
  <div class="lab" style="left:20px;top:130px;width:226px">Company's overview</div>
  <ul class="list" style="left:20px;top:140px;width:226px"><li>Key data from the entire presentation</li><li>Producer of high quality products A, B, C</li><li>Planned tripling of revenues and EBITDA</li><li>New product lines and foreign markets</li><li>Unique business model based on trust</li><li>Team with business and sales skills</li></ul>
  <div class="lab" style="left:268px;top:48px;width:228px">Unique selling points and market opportunities</div>
  <div class="abs" style="left:272px;top:62px;width:224px;display:flex;justify-content:space-around;font:4.3px 'Open Sans';color:var(--text)"><span>[graphics/photo/shape]</span><span>[graphics/photo/shape]</span><span>[graphics/photo/shape]</span></div>
  <div class="abs" style="left:272px;top:82px;width:224px;display:flex;justify-content:space-around;font:5.5px 'Open Sans';color:var(--ink)"><span>[description]</span><span>[description]</span><span>[description]</span></div>
  <div class="lab" style="left:268px;top:130px;width:228px">KPI's</div>
  <div class="tag" style="left:282px;top:143px;width:18px;height:11px">xx</div><div class="field" style="left:304px;top:143px;width:52px;height:11px">[employment increase]</div>
  <div class="tag" style="left:402px;top:143px;width:18px;height:11px">xx%</div><div class="field" style="left:424px;top:143px;width:56px;height:11px">[increase in clients]</div>
  <div class="tag" style="left:282px;top:162px;width:18px;height:11px">&gt;xxx</div><div class="field" style="left:304px;top:162px;width:52px;height:11px">[products sold]</div>
  <div class="tag" style="left:402px;top:162px;width:18px;height:11px">x,xx</div><div class="field" style="left:424px;top:162px;width:56px;height:11px">[average recipients]</div>
  <div class="tag" style="left:282px;top:181px;width:18px;height:11px">xx</div><div class="field" style="left:304px;top:181px;width:52px;height:11px">[production sites]</div>
  <div class="tag" style="left:402px;top:181px;width:18px;height:11px">xxx</div><div class="field" style="left:424px;top:181px;width:56px;height:11px">[order speed]</div>
  <div class="ft"><div class="n">4</div><div class="c">STRICTLY CONFIDENTIAL</div><div class="l">[Company logo]</div></div>
</section>

<!-- 5 Introduction with coverage -->
<section class="slide" style="left:22px;top:215px">
  <div class="title">INTRODUCTION</div><div class="sub">[Company] is a producer [...]</div><div class="rule"></div>
  <div class="logo"><i></i>BRIGHTVALE</div>
  <div class="lab" style="left:20px;top:48px;width:224px">Basic information</div>
  <div class="tag" style="left:20px;top:58px;width:42px;height:10px">Headquarters</div><div class="field" style="left:66px;top:58px;width:178px;height:10px">[address]</div>
  <div class="tag" style="left:20px;top:72px;width:42px;height:10px">Industry</div><div class="field" style="left:66px;top:72px;width:178px;height:10px">[name of the industry]</div>
  <div class="tag" style="left:20px;top:86px;width:42px;height:10px">Headcount</div><div class="field" style="left:66px;top:86px;width:178px;height:10px">[number of employees]</div>
  <div class="tag" style="left:20px;top:100px;width:42px;height:14px">Ownership structure</div><div class="field" style="left:66px;top:100px;width:178px;height:14px">x,xx% ◯ x,xx% &nbsp;• Shareholder 1 • Shareholder 2</div>
  <div class="lab" style="left:20px;top:120px;width:224px">Investment attractiveness</div>
  <ul class="list" style="left:20px;top:130px;width:224px"><li>Manufacturer of high quality product A, B, C</li><li>One of the widest product offers on the market</li><li>Order execution on average faster than rivals</li><li>Planned tripling of revenues and EBITDA</li><li>Absorbent market with steady growth rate</li><li>High specialisation and flexible production</li><li>Unique business model based on trust</li><li>Development strategy assuming growth</li></ul>
  <div class="lab" style="left:266px;top:48px;width:230px">Headquarters and geographical coverage</div>
  <div class="mapfill" role="img" aria-label="World map showing headquarters and geographical coverage" style="left:272px;top:58px;width:218px;height:84px;background:linear-gradient(180deg,#2a58a8,#1d3c86)"></div>
  <div class="lab" style="left:266px;top:150px;width:230px">KPI's</div>
  <div class="tag" style="left:288px;top:160px;width:20px;height:10px">+[x,xx]%</div><div class="field" style="left:312px;top:160px;width:52px;height:10px">Production volume</div>
  <div class="tag" style="left:400px;top:160px;width:20px;height:10px">+[x]%</div><div class="field" style="left:424px;top:160px;width:56px;height:10px">Revenue increase</div>
  <div class="tag" style="left:288px;top:176px;width:20px;height:10px">[x]</div><div class="field" style="left:312px;top:176px;width:52px;height:10px">Production plants</div>
  <div class="tag" style="left:400px;top:176px;width:20px;height:10px">&gt;[x]</div><div class="field" style="left:424px;top:176px;width:56px;height:10px">Number of recipients</div>
  <div class="tag" style="left:288px;top:192px;width:20px;height:10px">[x]</div><div class="field" style="left:312px;top:192px;width:52px;height:10px">Production plants</div>
  <div class="tag" style="left:400px;top:192px;width:20px;height:10px">&lt;[x]</div><div class="field" style="left:424px;top:192px;width:56px;height:10px">Contract execution</div>
  <div class="tag" style="left:288px;top:208px;width:20px;height:10px">~[x]</div><div class="field" style="left:312px;top:208px;width:52px;height:10px">Products developed</div>
  <div class="tag" style="left:400px;top:208px;width:20px;height:10px">+[x]%</div><div class="field" style="left:424px;top:208px;width:56px;height:10px">Employment growth</div>
  <div class="ft"><div class="n">5</div><div class="c">STRICTLY CONFIDENTIAL</div><div class="l">[Company logo]</div></div>
</section>

<!-- 6 Basic information -->
<section class="slide" style="left:333px;top:215px">
  <div class="title">BASIC INFORMATION</div><div class="sub">XXX is a fast-growing company delivering a wide choice of services</div><div class="rule"></div>
  <div class="logo"><i></i>BRIGHTVALE</div>
  <div class="lab" style="left:20px;top:48px;width:228px">Key financial results, PLN m</div>
  <svg class="svgabs" width="516" height="290">
    <g fill="#1f64bd"><rect x="40" y="128" width="8" height="12"/><rect x="70" y="104" width="8" height="36"/><rect x="100" y="90" width="8" height="50"/><rect x="130" y="82" width="8" height="58"/><rect x="160" y="98" width="8" height="42"/><rect x="190" y="72" width="8" height="68"/></g>
    <g fill="#1d3c86"><rect x="50" y="138" width="6" height="2"/><rect x="80" y="138" width="6" height="2"/><rect x="110" y="132" width="6" height="8"/><rect x="140" y="124" width="6" height="16"/><rect x="170" y="130" width="6" height="10"/><rect x="200" y="126" width="6" height="14"/></g>
    <polyline points="45,74 75,66 105,60 135,58 165,56 195,55" fill="none" stroke="#9dbde6" stroke-width=".8" stroke-dasharray="2 1.5"/>
    <line x1="30" y1="140" x2="220" y2="140" stroke="#c4ccd8" stroke-width=".6"/>
    <rect x="96" y="78" width="20" height="5" fill="#1d3c86"/><rect x="140" y="114" width="20" height="5" fill="#1d3c86"/>
  </svg>
  <table class="grid" style="left:24px;top:160px;width:220px;font-size:3.6px">
    <tr><th>Financial results</th><th>2016</th><th>2017</th><th>2018</th><th>2019</th><th>2020</th></tr>
    <tr><td>Revenue</td><td>Xxx</td><td>Xxx</td><td>Xxx</td><td>Xxx</td><td>Xxx</td></tr>
    <tr><td>Adj. EBITDA</td><td>Xxx</td><td>Xxx</td><td>Xxx</td><td>Xxx</td><td>Xxx</td></tr>
    <tr><td>EBITDA margin</td><td>Xx%</td><td>Xx%</td><td>Xx%</td><td>Xx%</td><td>Xx%</td></tr>
    <tr><td>Profit before tax</td><td>Xxx</td><td>Xxx</td><td>Xxx</td><td>Xxx</td><td>Xxx</td></tr>
    <tr><td>Net income</td><td>Xxx</td><td>Xxx</td><td>Xxx</td><td>Xxx</td><td>Xxx</td></tr>
    <tr><td>Net debt</td><td>Xxx</td><td>Xxx</td><td>Xxx</td><td>Xxx</td><td>Xxx</td></tr>
  </table>
  <div class="lab" style="left:268px;top:48px;width:228px">Commentary</div>
  <div class="card" style="left:268px;top:58px;width:228px;height:200px"><ul class="list dots" style="left:10px;top:8px;width:210px"><li>Between 20XX and 20XX the company reported dynamic growth, increasing net profit margin.</li><li>Year 20XX is considered a transition period, in which:<br>– one-time expenses were incurred<br>– the company started to integrate portfolio<br>– high standards of services were kept</li><li>Thanks to financing obtained, the company is forecasted to return to a natural, fast development path.</li></ul></div>
  <div class="ft"><div class="n">6</div><div class="c">STRICTLY CONFIDENTIAL</div><div class="l">[Company logo]</div></div>
</section>

<!-- 7 Business development -->
<section class="slide" style="left:641px;top:215px">
  <div class="title">BUSINESS DEVELOPMENT</div><div class="sub">[Heading to business development]</div><div class="rule"></div>
  <div class="logo"><i></i>BRIGHTVALE</div>
  <div class="lab" style="left:20px;top:48px;width:220px">Business story</div>
  <ul class="list" style="left:20px;top:58px;width:220px"><li>[How the business idea was born]</li><li>[What inspired the founders]</li><li>[What problem the company wants to solve]</li></ul>
  <div class="lab" style="left:264px;top:48px;width:232px">Development history</div>
  <ul class="list dots" style="left:264px;top:58px;width:232px"><li>The company was registered in [...]. The first product was sold in [...]</li><li>The company started its activity from offering services [...]</li><li>Responding to market needs of the Management Board [...]</li><li>The Board also decided on a geographical expansion [...]</li></ul>
  <div class="lab" style="left:20px;top:136px;width:476px">History and milestones</div>
  <svg class="svgabs" width="516" height="290">
    <line x1="50" y1="172" x2="480" y2="172" stroke="#9dbde6" stroke-width="1"/>
    <g fill="#1d3c86"><circle cx="50" cy="172" r="4"/><circle cx="136" cy="172" r="4"/><circle cx="222" cy="172" r="4"/><circle cx="308" cy="172" r="4"/><circle cx="394" cy="172" r="4"/><circle cx="480" cy="172" r="4"/></g>
    <g stroke="#9dbde6" stroke-width=".8"><line x1="50" y1="176" x2="50" y2="186"/><line x1="136" y1="176" x2="136" y2="186"/><line x1="222" y1="176" x2="222" y2="186"/><line x1="308" y1="176" x2="308" y2="186"/><line x1="394" y1="176" x2="394" y2="186"/><line x1="480" y1="176" x2="480" y2="186"/></g>
    <g font-family="Montserrat" font-size="4.5" font-weight="700" fill="#2b7fd6" text-anchor="middle"><text x="50" y="162">2015</text><text x="136" y="162">2016</text><text x="222" y="162">2017</text><text x="308" y="162">2018</text><text x="394" y="162">2019</text><text x="480" y="162">2020</text></g>
    <g font-family="Open Sans" font-size="3.8" fill="#8c9db4" text-anchor="middle"><text x="50" y="194">PROJECT NAME</text><text x="136" y="194">PROJECT NAME</text><text x="222" y="194">PROJECT NAME</text><text x="308" y="194">PROJECT NAME</text><text x="394" y="194">PROJECT NAME</text><text x="480" y="194">PROJECT NAME</text></g>
    <g font-family="Open Sans" font-size="3.5" fill="#3a4556" text-anchor="middle"><text x="50" y="202">Short milestone note</text><text x="136" y="202">Short milestone note</text><text x="222" y="202">Short milestone note</text><text x="308" y="202">Short milestone note</text><text x="394" y="202">Short milestone note</text><text x="480" y="202">Short milestone note</text></g>
  </svg>
  <div class="ft"><div class="n">7</div><div class="c">STRICTLY CONFIDENTIAL</div><div class="l">[Company logo]</div></div>
</section>

<!-- 9 Development plans -->
<section class="slide" style="left:22px;top:409px">
  <div class="title">DEVELOPMENT PLANS</div><div class="sub" style="letter-spacing:.3px;width:360px">[The company] focuses on responding to the growing needs of the market, prioritising directions of development</div><div class="rule" style="top:40px"></div>
  <div class="logo"><i></i>BRIGHTVALE</div>
  <div class="lab" style="left:20px;top:48px;width:290px">Strategic development directions for 2019-2022</div>
  <div class="pill" style="left:20px;top:60px;width:60px;height:12px">Sales growth</div>
  <div class="pill" style="left:20px;top:98px;width:60px;height:12px">Geographical development</div>
  <div class="pill" style="left:20px;top:136px;width:60px;height:12px">Increasing capacity</div>
  <div class="pill" style="left:20px;top:168px;width:60px;height:12px">Product mix</div>
  <div class="pill" style="left:20px;top:204px;width:60px;height:12px">Process efficiency</div>
  <ul class="list dots" style="left:90px;top:58px;width:220px;font-size:3.5px"><li>Sales increase to approx. PLN [xx] million in 20xx</li><li>Sustained increase in EBITDA margin</li><li>Increase in net working capital</li></ul>
  <ul class="list dots" style="left:90px;top:96px;width:220px;font-size:3.5px"><li>Reinforcing a strong position in the current market</li><li>Entering new customer segments</li><li>Planned doubling of the customer base</li></ul>
  <ul class="list dots" style="left:90px;top:136px;width:220px;font-size:3.5px"><li>Increase in plant efficiency</li><li>Expansion [...]</li></ul>
  <ul class="list dots" style="left:90px;top:166px;width:220px;font-size:3.5px"><li>Expanding the portfolio of offered products</li><li>Development of high-margin product groups</li></ul>
  <ul class="list dots" style="left:90px;top:200px;width:220px;font-size:3.5px"><li>Reducing losses of raw materials</li><li>Optimal use of current machines</li><li>A leap in production efficiency</li></ul>
  <div class="lab" style="left:320px;top:48px;width:176px">Revenue and EBITDA, 2019P-2022P</div>
  <div class="lab" style="left:320px;top:150px;width:176px">Sales volumes, 2019P-2022P</div>
  <svg class="svgabs" width="516" height="290">
    <rect x="320" y="58" width="176" height="84" fill="#fff"/><rect x="320" y="162" width="176" height="86" fill="#fff"/>
    <g fill="#1f64bd"><rect x="340" y="120" width="8" height="12"/><rect x="380" y="110" width="8" height="22"/><rect x="420" y="92" width="8" height="40"/><rect x="460" y="72" width="8" height="60"/><rect x="345" y="220" width="8" height="18"/><rect x="385" y="200" width="8" height="38"/><rect x="425" y="190" width="8" height="48"/><rect x="465" y="178" width="8" height="60"/></g>
    <g fill="#1d3c86"><rect x="349" y="128" width="6" height="4"/><rect x="389" y="124" width="6" height="8"/><rect x="429" y="120" width="6" height="12"/><rect x="469" y="116" width="6" height="16"/></g>
    <rect x="354" y="64" width="22" height="5" fill="#1d3c86"/><rect x="356" y="168" width="22" height="5" fill="#1d3c86"/>
  </svg>
  <div class="ft"><div class="n">9</div><div class="c">STRICTLY CONFIDENTIAL</div><div class="l">[Company logo]</div></div>
</section>

<!-- 10 Text and table -->
<section class="slide" style="left:333px;top:409px">
  <div class="title">YOUR AWESOME TEXT GOES HERE</div><div class="sub">Sub title goes here</div><div class="rule"></div>
  <div class="logo"><i></i>BRIGHTVALE</div>
  <div class="lab" style="left:20px;top:64px;width:180px">Your awesome text here</div>
  <ul class="list dots" style="left:24px;top:78px;width:176px;font-size:4.2px"><li>Sales increase to approx. PLN [xx] million in 20xx, compared to PLN [xx] million in 20xx</li><li>Sustained increase in EBITDA margin</li><li>Increase in net working capital, among others</li></ul>
  <div class="lab" style="left:20px;top:156px;width:180px">Your awesome text here</div>
  <ul class="list dots" style="left:24px;top:170px;width:176px;font-size:4.2px"><li>Sales increase to approx. PLN [xx] million in 20xx, compared to PLN [xx] million in 20xx</li><li>Sustained increase in EBITDA margin</li><li>Increase in net working capital, among others</li></ul>
  <div class="lab" style="left:214px;top:42px;width:282px">Revenue and EBITDA, 2019P-2022P [thousand PLN]</div>
  <table class="grid" style="left:214px;top:54px;width:282px">
    <tr><th>(kSEK)</th><th>Text</th><th>Text</th><th>Text</th><th>Text</th><th>Text</th></tr>
    <tr><td>Text</td><td>5 000</td><td>5 000</td><td>5 000</td><td>5 000</td><td>5 000</td></tr>
    <tr><td>Text</td><td>4 000</td><td>4 000</td><td>4 000</td><td>4 000</td><td>4 000</td></tr>
    <tr><td>Text</td><td>-1 000</td><td>-1 000</td><td>-1 000</td><td>-1 000</td><td>-1 000</td></tr>
    <tr><td>Text</td><td>-1 000</td><td>-1 000</td><td>-1 000</td><td>-1 000</td><td>-1 000</td></tr>
    <tr><td>Text</td><td>-1 000</td><td>-1 000</td><td>-1 000</td><td>-1 000</td><td>-1 000</td></tr>
    <tr><td>Text</td><td>-500</td><td>-500</td><td>-500</td><td>-500</td><td>-500</td></tr>
    <tr class="b"><td>Text</td><td>500</td><td>500</td><td>500</td><td>500</td><td>500</td></tr>
    <tr><td>Text</td><td>-100</td><td>-100</td><td>-100</td><td>-100</td><td>-100</td></tr>
    <tr class="b"><td>Text</td><td>400</td><td>400</td><td>400</td><td>400</td><td>400</td></tr>
    <tr><td>Text</td><td>100</td><td>100</td><td>100</td><td>100</td><td>100</td></tr>
    <tr class="b"><td>Text</td><td>500</td><td>500</td><td>500</td><td>500</td><td>500</td></tr>
  </table>
  <div class="ft"><div class="n">10</div><div class="c">STRICTLY CONFIDENTIAL</div><div class="l">[Company logo]</div></div>
</section>

<!-- 11 Donut, bars, dark table -->
<section class="slide" style="left:641px;top:409px">
  <div class="title">YOUR AWESOME TEXT GOES HERE</div><div class="sub">Sub title goes here</div><div class="rule"></div>
  <div class="logo"><i></i>BRIGHTVALE</div>
  <div class="lab" style="left:20px;top:48px;width:170px">Your awesome text here</div>
  <div class="lab" style="left:20px;top:146px;width:170px">Your awesome text here</div>
  <svg class="svgabs" width="516" height="290">
    <g transform="translate(66 88)" fill="none" stroke-width="7">
      <circle r="14" stroke="#1d3c86" stroke-dasharray="26 62" />
      <circle r="14" stroke="#1f64bd" stroke-dasharray="18 70" stroke-dashoffset="-26"/>
      <circle r="14" stroke="#2b7fd6" stroke-dasharray="16 72" stroke-dashoffset="-44"/>
      <circle r="14" stroke="#8c9db4" stroke-dasharray="14 74" stroke-dashoffset="-60"/>
      <circle r="14" stroke="#c4ccd8" stroke-dasharray="14 74" stroke-dashoffset="-74"/>
    </g>
    <g font-family="Open Sans" font-size="3.5" fill="#3a4556"><text x="120" y="74">• Category 1</text><text x="120" y="82">• Category 2</text><text x="120" y="90">• Category 3</text><text x="120" y="98">• Category 4</text><text x="120" y="106">• Category 5</text></g>
    <g fill="#1f64bd"><rect x="34" y="230" width="8" height="8"/><rect x="66" y="226" width="8" height="12"/><rect x="98" y="222" width="8" height="16"/><rect x="130" y="212" width="8" height="26"/><rect x="162" y="206" width="8" height="32"/></g>
    <g font-family="Open Sans" font-size="3.5" fill="#3a4556" text-anchor="middle"><text x="38" y="226">55 000</text><text x="70" y="222">60 000</text><text x="102" y="218">80 000</text><text x="134" y="208">120 000</text><text x="166" y="202">135 000</text><text x="38" y="244">20XX</text><text x="70" y="244">20XX</text><text x="102" y="244">20XX</text><text x="134" y="244">20XX</text><text x="166" y="244">20XX</text></g>
  </svg>
  <div class="lab" style="left:210px;top:48px;width:286px">Revenue and EBITDA, 2019P-2022P [thousand PLN]</div>
  <div class="abs" style="left:210px;top:58px;width:60px;height:186px;background:var(--navy)"></div>
  <table class="grid" style="left:210px;top:58px;width:286px;font-size:4px">
    <tr><th>(kSEK)</th><th>Text</th><th>Text</th><th>Text</th><th>Text</th><th>Text</th></tr>
    <tr><td style="color:#fff">Text</td><td>5 000</td><td>5 000</td><td>5 000</td><td>5 000</td><td>5 000</td></tr>
    <tr><td style="color:#fff">Text</td><td>4 000</td><td>4 000</td><td>4 000</td><td>4 000</td><td>4 000</td></tr>
    <tr><td style="color:#fff">Text</td><td>-1 000</td><td>-1 000</td><td>-1 000</td><td>-1 000</td><td>-1 000</td></tr>
    <tr><td style="color:#fff">Text</td><td>-1 000</td><td>-1 000</td><td>-1 000</td><td>-1 000</td><td>-1 000</td></tr>
    <tr><td style="color:#fff">Text</td><td>-1 000</td><td>-1 000</td><td>-1 000</td><td>-1 000</td><td>-1 000</td></tr>
    <tr><td style="color:#fff">Text</td><td>-500</td><td>-500</td><td>-500</td><td>-500</td><td>-500</td></tr>
    <tr class="b"><td style="color:#fff">Text</td><td>500</td><td>500</td><td>500</td><td>500</td><td>500</td></tr>
    <tr><td style="color:#fff">Text</td><td>-100</td><td>-100</td><td>-100</td><td>-100</td><td>-100</td></tr>
    <tr class="b"><td style="color:#fff">Text</td><td>400</td><td>400</td><td>400</td><td>400</td><td>400</td></tr>
    <tr><td style="color:#fff">Text</td><td>100</td><td>100</td><td>100</td><td>100</td><td>100</td></tr>
    <tr class="b"><td style="color:#fff">Text</td><td>500</td><td>500</td><td>500</td><td>500</td><td>500</td></tr>
  </table>
  <div class="ft"><div class="n">11</div><div class="c">STRICTLY CONFIDENTIAL</div><div class="l">[Company logo]</div></div>
</section>

<!-- 12 Europe coverage -->
<section class="slide" style="left:22px;top:604px">
  <div class="title">YOUR AWESOME TEXT GOES HERE</div><div class="sub">Sub title goes here</div><div class="rule"></div>
  <div class="logo" style="z-index:2"><i></i>BRIGHTVALE</div>
  <div class="card" style="left:20px;top:48px;width:170px;height:64px"></div>
  <div class="tag" style="left:30px;top:72px;width:58px;height:11px;border-radius:3px">YOUR AWESOME HERE</div>
  <ul class="list dots" style="left:114px;top:58px;font-size:4.2px"><li>Your Text Goes Here</li><li>Your Text Goes Here</li><li>Your Text Goes Here</li><li>Your Text Goes Here</li><li>Your Text Goes Here</li><li>Your Text Goes Here</li></ul>
  <div class="lab" style="left:20px;top:128px;width:170px">Your awesome text here</div>
  <svg class="svgabs" width="516" height="290">
    <g fill="#1d3c86"><rect x="30" y="228" width="8" height="12"/><rect x="62" y="224" width="8" height="16"/><rect x="94" y="220" width="8" height="20"/><rect x="126" y="210" width="8" height="30"/><rect x="158" y="204" width="8" height="36"/></g>
    <g font-family="Open Sans" font-size="3.5" fill="#3a4556" text-anchor="middle"><text x="34" y="224">55 000</text><text x="66" y="220">60 000</text><text x="98" y="216">80 000</text><text x="130" y="206">120 000</text><text x="162" y="200">135 000</text><text x="34" y="246">20XX</text><text x="66" y="246">20XX</text><text x="98" y="246">20XX</text><text x="130" y="246">20XX</text><text x="162" y="246">20XX</text></g>
  </svg>
  <div class="mapfill" role="img" aria-label="Map of Europe with highlighted countries of operation" style="left:232px;top:14px;width:270px;height:254px;border-radius:40%;background:radial-gradient(circle at 40% 65%,#1d3c86 0%,#2a4f96 45%,#8c9db4 75%,rgba(140,157,180,0) 100%)"></div>
  <div class="ft"><div class="n">12</div><div class="c">STRICTLY CONFIDENTIAL</div><div class="l">[Company logo]</div></div>
</section>

<!-- 13 Stats, text panels, table -->
<section class="slide" style="left:333px;top:604px">
  <div class="title">YOUR AWESOME TEXT GOES HERE</div><div class="sub">Sub title goes here</div><div class="rule"></div>
  <div class="logo"><i></i>BRIGHTVALE</div>
  <div class="stat" style="left:28px;top:46px;width:140px;height:58px"><p>Lorem ipsum is simply dummy text of the printing and typesetting industry.</p><b>310</b></div>
  <div class="stat mid" style="left:186px;top:46px;width:140px;height:58px"><p>Lorem ipsum is simply dummy text of the printing and typesetting industry.</p><b>150</b></div>
  <div class="stat" style="left:344px;top:46px;width:140px;height:58px"><p>Lorem ipsum is simply dummy text of the printing and typesetting industry.</p><b>9.010</b></div>
  <div class="lab" style="left:20px;top:116px;width:200px">Revenue and EBITDA, 2019P-2022P [thousand PLN]</div>
  <div class="pill" style="left:20px;top:128px;width:200px;height:10px;justify-content:flex-start;padding-left:8px">Your Text Here</div>
  <ul class="list dots" style="left:26px;top:141px;width:190px;font-size:3.6px"><li>Sales increase to approx. PLN [xx] million in 20xx</li><li>Sustained increase in EBITDA margin</li><li>Increase in net working capital</li></ul>
  <div class="pill" style="left:20px;top:188px;width:200px;height:10px;justify-content:flex-start;padding-left:8px">Your Text Here</div>
  <ul class="list dots" style="left:26px;top:201px;width:190px;font-size:3.6px"><li>Sales increase to approx. PLN [xx] million in 20xx</li><li>Sustained increase in EBITDA margin</li><li>Increase in net working capital</li></ul>
  <div class="lab" style="left:232px;top:116px;width:264px">Revenue and EBITDA, 2019P-2022P [thousand PLN]</div>
  <div class="card" style="left:232px;top:128px;width:264px;height:128px"></div>
  <table class="grid" style="left:238px;top:132px;width:252px;font-size:3.7px">
    <tr><th>(kSEK)</th><th>Text</th><th>Text</th><th>Text</th><th>Text</th><th>Text</th></tr>
    <tr><td>Text</td><td>5 000</td><td>5 000</td><td>5 000</td><td>5 000</td><td>5 000</td></tr>
    <tr><td>Text</td><td>4 000</td><td>4 000</td><td>4 000</td><td>4 000</td><td>4 000</td></tr>
    <tr><td>Text</td><td>-1 000</td><td>-1 000</td><td>-1 000</td><td>-1 000</td><td>-1 000</td></tr>
    <tr><td>Text</td><td>-1 000</td><td>-1 000</td><td>-1 000</td><td>-1 000</td><td>-1 000</td></tr>
    <tr><td>Text</td><td>-500</td><td>-500</td><td>-500</td><td>-500</td><td>-500</td></tr>
    <tr class="b"><td>Text</td><td>500</td><td>500</td><td>500</td><td>500</td><td>500</td></tr>
    <tr><td>Text</td><td>-100</td><td>-100</td><td>-100</td><td>-100</td><td>-100</td></tr>
    <tr class="b"><td>Text</td><td>400</td><td>400</td><td>400</td><td>400</td><td>400</td></tr>
    <tr><td>Text</td><td>100</td><td>100</td><td>100</td><td>100</td><td>100</td></tr>
    <tr class="b"><td>Text</td><td>500</td><td>500</td><td>500</td><td>500</td><td>500</td></tr>
  </table>
  <div class="ft"><div class="n">13</div><div class="c">STRICTLY CONFIDENTIAL</div><div class="l">[Company logo]</div></div>
</section>

<!-- 14 Structure tree -->
<section class="slide" style="left:641px;top:604px">
  <div class="title">YOUR AWESOME TEXT GOES HERE</div><div class="sub">Sub title goes here</div><div class="rule"></div>
  <div class="logo"><i></i>BRIGHTVALE</div>
  <svg class="svgabs" width="516" height="290">
    <g fill="none" stroke="#8c9db4" stroke-width=".8">
      <path d="M88 148 H108 M108 82 V204 M108 82 H118 M108 148 H118 M108 204 H118"/>
      <path d="M196 82 H206 M206 68 V96 M206 68 H216 M206 96 H216"/>
      <path d="M196 148 H216"/>
      <path d="M196 204 H206 M206 190 V218 M206 190 H216 M206 218 H216"/>
    </g>
  </svg>
  <div class="pill" style="left:36px;top:140px;width:58px;height:16px;background:var(--blue);justify-content:flex-start;padding-left:22px">Lorem Ipsum<span class="abs" style="left:3px;top:3px;width:10px;height:10px;border-radius:50%;background:#fff"></span></div>
  <div class="pill" style="left:114px;top:74px;width:84px;height:16px;background:var(--slate);justify-content:flex-start;padding-left:24px">Lorem Ipsum<span class="abs" style="left:3px;top:3px;width:10px;height:10px;border-radius:50%;background:#fff"></span></div>
  <div class="pill" style="left:114px;top:140px;width:84px;height:16px;background:var(--slate);justify-content:flex-start;padding-left:24px">Lorem Ipsum<span class="abs" style="left:3px;top:3px;width:10px;height:10px;border-radius:50%;background:#fff"></span></div>
  <div class="pill" style="left:114px;top:196px;width:84px;height:16px;background:var(--slate);justify-content:flex-start;padding-left:24px">Lorem Ipsum<span class="abs" style="left:3px;top:3px;width:10px;height:10px;border-radius:50%;background:#fff"></span></div>
  <div class="pill" style="left:216px;top:63px;width:48px;height:10px">Name</div><div class="pill" style="left:280px;top:63px;width:48px;height:10px">Name</div><div class="pill" style="left:344px;top:63px;width:48px;height:10px">Name</div>
  <div class="pill" style="left:216px;top:91px;width:48px;height:10px">Name</div><div class="pill" style="left:280px;top:91px;width:48px;height:10px">Name</div>
  <div class="pill" style="left:216px;top:143px;width:48px;height:10px">Name</div><div class="pill" style="left:280px;top:143px;width:48px;height:10px">Name</div><div class="pill" style="left:344px;top:143px;width:48px;height:10px">Name</div>
  <div class="pill" style="left:216px;top:185px;width:48px;height:10px">Name</div>
  <div class="pill" style="left:216px;top:213px;width:48px;height:10px">Name</div><div class="pill" style="left:280px;top:213px;width:48px;height:10px">Name</div>
  <div class="ft"><div class="n">14</div><div class="c">STRICTLY CONFIDENTIAL</div><div class="l">[Company logo]</div></div>
</section>

<!-- 15 Factors -->
<section class="slide" style="left:22px;top:804px">
  <div class="title">YOUR AWESOME TEXT GOES HERE</div><div class="sub">Sub title goes here</div><div class="rule"></div>
  <div class="logo"><i></i>BRIGHTVALE</div>
  <div class="lab" style="left:20px;top:48px;width:476px">Current [May 2019] factors of company development on the market in Poland [%]</div>
  <svg class="svgabs" width="516" height="290">
    <g><rect x="90" y="64" width="30" height="3" fill="#c4ccd8"/><rect x="90" y="68" width="100" height="3" fill="#9dbde6"/><rect x="90" y="72" width="160" height="3" fill="#8c9db4"/><rect x="90" y="76" width="50" height="3" fill="#1f64bd"/><rect x="90" y="80" width="320" height="3" fill="#1d3c86"/><rect x="90" y="84" width="120" height="3" fill="#2b7fd6"/><rect x="90" y="88" width="180" height="3" fill="#1f64bd"/></g>
    <line x1="90" y1="60" x2="90" y2="96" stroke="#c4ccd8" stroke-width=".6"/>
    <g font-family="Open Sans" font-size="3.5" fill="#3a4556"><text x="60" y="80">V 2019</text><text x="88" y="102">0%</text><text x="150" y="102">5%</text><text x="210" y="102">10%</text><text x="270" y="102">15%</text><text x="330" y="102">20%</text><text x="390" y="102">25%</text><text x="450" y="102">30%</text></g>
    <g font-family="Open Sans" font-size="3.2" fill="#3a4556"><text x="80" y="112">■ External financing ■ Marketing ■ Legal changes ■ Notification process ■ Offer ■ Growth</text></g>
  </svg>
  <div class="lab" style="left:20px;top:118px;width:476px">Current [May 2019] factors of company development on the market in Poland [%]</div>
  <div class="card" style="left:216px;top:136px;width:84px;height:14px;border-radius:7px;display:flex;align-items:center;justify-content:center;font:600 6px 'Open Sans';color:var(--navy)">NAME</div>
  <svg class="svgabs" width="516" height="290"><path d="M258 150 V160 M58 160 H458 M58 160 V166 M158 160 V166 M258 160 V166 M358 160 V166 M458 160 V166" stroke="#8c9db4" stroke-width=".7" fill="none"/></svg>
  <div class="pill" style="left:28px;top:166px;width:60px;height:13px;background:var(--blue)">NAME</div>
  <div class="pill" style="left:128px;top:166px;width:60px;height:13px;background:var(--blue)">NAME</div>
  <div class="pill" style="left:228px;top:166px;width:60px;height:13px;background:var(--blue)">NAME</div>
  <div class="pill" style="left:328px;top:166px;width:60px;height:13px;background:var(--blue)">NAME</div>
  <div class="pill" style="left:428px;top:166px;width:60px;height:13px;background:var(--blue)">NAME</div>
  <div class="abs" style="left:28px;top:184px;width:460px;display:flex;justify-content:space-between;font:600 4px 'Open Sans';color:var(--ink);text-align:center"><span style="width:60px">Lorem ipsum dolor sit amet.</span><span style="width:60px">Lorem ipsum dolor sit amet.</span><span style="width:60px">Lorem ipsum dolor sit amet.</span><span style="width:60px">Lorem ipsum dolor sit amet.</span><span style="width:60px">Lorem ipsum dolor sit amet.</span></div>
  <div class="ft"><div class="n">15</div><div class="c">STRICTLY CONFIDENTIAL</div><div class="l">[Company logo]</div></div>
</section>

<!-- 16 Key people -->
<section class="slide" style="left:333px;top:804px">
  <div class="title">KEY PEOPLE AND ORGANISATIONAL STRUCTURE</div><div class="sub" style="letter-spacing:.3px">Experienced leaders who are industry experts, rooted in the culture of growth</div><div class="rule"></div>
  <div class="logo"><i></i>BRIGHTVALE</div>
  <div class="lab" style="left:20px;top:46px;width:476px">Key people</div>
  <div class="card" style="left:20px;top:56px;width:222px;height:74px"></div>
  <div class="abs" style="left:20px;top:56px;width:8px;height:74px;background:var(--blue)"></div>
  <div class="abs" style="left:36px;top:62px;font:600 6px 'Open Sans';color:var(--blue)">CEO</div>
  <div class="abs" style="left:36px;top:78px;font:4.2px 'Open Sans'">[Photo]</div>
  <div class="abs" style="left:36px;top:118px;font:600 4.2px 'Open Sans';color:var(--blue)">[name]</div>
  <div class="tag" style="left:108px;top:62px;width:32px;height:5px;border-radius:3px;font-size:3px">In the company</div><div class="abs" style="left:146px;top:62px;font:3.6px 'Open Sans'">[description]</div>
  <div class="tag" style="left:108px;top:86px;width:32px;height:5px;border-radius:3px;font-size:3px">Previous positions</div><div class="abs" style="left:146px;top:86px;font:3.6px 'Open Sans'">[description]</div>
  <div class="tag" style="left:108px;top:110px;width:32px;height:5px;border-radius:3px;font-size:3px">Education</div><div class="abs" style="left:146px;top:110px;font:3.6px 'Open Sans'">[description]</div>
  <div class="card" style="left:262px;top:56px;width:222px;height:74px"></div>
  <div class="abs" style="left:262px;top:56px;width:8px;height:74px;background:var(--blue)"></div>
  <div class="abs" style="left:278px;top:62px;font:600 6px 'Open Sans';color:var(--blue)">COO</div>
  <div class="abs" style="left:278px;top:78px;font:4.2px 'Open Sans'">[Photo]</div>
  <div class="abs" style="left:278px;top:118px;font:600 4.2px 'Open Sans';color:var(--blue)">[name]</div>
  <div class="tag" style="left:350px;top:62px;width:32px;height:5px;border-radius:3px;font-size:3px">In the company</div><div class="abs" style="left:388px;top:62px;font:3.6px 'Open Sans'">[description]</div>
  <div class="tag" style="left:350px;top:86px;width:32px;height:5px;border-radius:3px;font-size:3px">Previous positions</div><div class="abs" style="left:388px;top:86px;font:3.6px 'Open Sans'">[description]</div>
  <div class="tag" style="left:350px;top:110px;width:32px;height:5px;border-radius:3px;font-size:3px">Education</div><div class="abs" style="left:388px;top:110px;font:3.6px 'Open Sans'">[description]</div>
  <div class="abs" style="left:20px;top:140px;width:464px;display:flex;justify-content:space-between">
    <div class="card" style="position:relative;width:70px;height:96px;font:4px 'Open Sans';text-align:center"><div style="padding-top:4px;color:var(--ink)">Director 1</div><div style="background:var(--blue);color:#fff;margin:2px 4px;font-size:3.4px">Information</div><div style="font-size:3.2px">[description of information]</div></div>
    <div class="card" style="position:relative;width:70px;height:96px;font:4px 'Open Sans';text-align:center"><div style="padding-top:4px;color:var(--ink)">Director 2</div><div style="background:var(--blue);color:#fff;margin:2px 4px;font-size:3.4px">Information</div><div style="font-size:3.2px">[description of information]</div></div>
    <div class="card" style="position:relative;width:70px;height:96px;font:4px 'Open Sans';text-align:center"><div style="padding-top:4px;color:var(--ink)">Director 3</div><div style="background:var(--blue);color:#fff;margin:2px 4px;font-size:3.4px">Information</div><div style="font-size:3.2px">[description of information]</div></div>
    <div class="card" style="position:relative;width:70px;height:96px;font:4px 'Open Sans';text-align:center"><div style="padding-top:4px;color:var(--ink)">Director 4</div><div style="background:var(--blue);color:#fff;margin:2px 4px;font-size:3.4px">Information</div><div style="font-size:3.2px">[description of information]</div></div>
    <div class="card" style="position:relative;width:70px;height:96px;font:4px 'Open Sans';text-align:center"><div style="padding-top:4px;color:var(--ink)">Director 5</div><div style="background:var(--blue);color:#fff;margin:2px 4px;font-size:3.4px">Information</div><div style="font-size:3.2px">[description of information]</div></div>
    <div class="card" style="position:relative;width:70px;height:96px;font:4px 'Open Sans';text-align:center"><div style="padding-top:4px;color:var(--ink)">Director 6</div><div style="background:var(--blue);color:#fff;margin:2px 4px;font-size:3.4px">Information</div><div style="font-size:3.2px">[description of information]</div></div>
  </div>
  <div class="ft"><div class="n">16</div><div class="c">STRICTLY CONFIDENTIAL</div><div class="l">[Company logo]</div></div>
</section>

<!-- 17 Competitive advantages -->
<section class="slide" style="left:641px;top:804px">
  <div class="title">COMPETITIVE ADVANTAGES</div><div class="sub" style="letter-spacing:.3px">Built competitive advantages allow the company to consistently strengthen its position</div><div class="rule"></div>
  <div class="logo"><i></i>BRIGHTVALE</div>
  <div class="lab" style="left:20px;top:48px;width:226px">Competitive advantages in terms of customer acquisition</div>
  <ul class="list dots" style="left:22px;top:58px;width:222px;font-size:3.7px"><li>Fastest response time to customer inquiry</li><li>One of the widest offers on the market</li><li>Having ready product registrations</li><li>Direct involvement of the company's authorities</li><li>Flexible machine changeover process</li><li>Strong commitment to the trade fair industry</li><li>Comprehensive, free of charge services</li><li>No sales [...]</li></ul>
  <div class="lab" style="left:266px;top:48px;width:230px">Competitive advantages in terms of contract execution time</div>
  <div class="tag" style="left:328px;top:58px;width:78px;height:9px">[Company logo]</div><div class="tag" style="left:412px;top:58px;width:78px;height:9px">Competition</div>
  <div class="tag" style="left:268px;top:72px;width:56px;height:11px;background:var(--navy);font-size:3.3px">Comprehensive product offer</div><div class="field" style="left:328px;top:72px;width:78px;height:11px;justify-content:center;padding:0;color:var(--blue)">[Description]</div><div class="field" style="left:412px;top:72px;width:78px;height:11px;justify-content:center;padding:0;color:var(--blue)">[Description]</div>
  <div class="tag" style="left:268px;top:87px;width:56px;height:11px;background:var(--navy);font-size:3.3px">Documentation</div><div class="field" style="left:328px;top:87px;width:78px;height:11px;justify-content:center;padding:0;color:var(--blue)">[Description]</div><div class="field" style="left:412px;top:87px;width:78px;height:11px;justify-content:center;padding:0;color:var(--blue)">[Description]</div>
  <div class="tag" style="left:268px;top:102px;width:56px;height:11px;background:var(--navy);font-size:3.3px">Standard order processing</div><div class="field" style="left:328px;top:102px;width:78px;height:11px;justify-content:center;padding:0;color:var(--blue)">[Description]</div><div class="field" style="left:412px;top:102px;width:78px;height:11px;justify-content:center;padding:0;color:var(--blue)">[Description]</div>
  <div class="tag" style="left:268px;top:117px;width:56px;height:11px;background:var(--navy);font-size:3.3px">Response to inquiry</div><div class="field" style="left:328px;top:117px;width:78px;height:11px;justify-content:center;padding:0;color:var(--blue)">[Description]</div><div class="field" style="left:412px;top:117px;width:78px;height:11px;justify-content:center;padding:0;color:var(--blue)">[Description]</div>
  <div class="lab" style="left:20px;top:142px;width:476px">Operational competitive advantages</div>
  <div class="tag" style="left:20px;top:154px;width:66px;height:13px;background:var(--navy)">Investments in certification</div><div class="field" style="left:90px;top:154px;width:150px;height:13px;justify-content:center;padding:0;color:var(--blue)">[Description]</div>
  <div class="tag" style="left:20px;top:174px;width:66px;height:13px;background:var(--navy)">High capacity utilisation</div><div class="field" style="left:90px;top:174px;width:150px;height:13px;justify-content:center;padding:0;color:var(--blue)">[Description]</div>
  <div class="tag" style="left:20px;top:194px;width:66px;height:13px;background:var(--navy)">Internal promotions</div><div class="field" style="left:90px;top:194px;width:150px;height:13px;justify-content:center;padding:0;color:var(--blue)">[Description]</div>
  <div class="tag" style="left:266px;top:154px;width:66px;height:13px;background:var(--navy)">Grant acquisition</div><div class="field" style="left:336px;top:154px;width:156px;height:13px;justify-content:center;padding:0;color:var(--blue)">[Description]</div>
  <div class="tag" style="left:266px;top:174px;width:66px;height:13px;background:var(--navy)">Manufacturing innovation</div><div class="field" style="left:336px;top:174px;width:156px;height:13px;justify-content:center;padding:0;color:var(--blue)">[Description]</div>
  <div class="tag" style="left:266px;top:194px;width:66px;height:13px;background:var(--navy)">New product registration</div><div class="field" style="left:336px;top:194px;width:156px;height:13px;justify-content:center;padding:0;color:var(--blue)">[Description]</div>
  <div class="ft"><div class="n">17</div><div class="c">STRICTLY CONFIDENTIAL</div><div class="l">[Company logo]</div></div>
</section>

<!-- 18 Stats and line chart -->
<section class="slide big" style="left:165px;top:995px">
  <div class="title">YOUR AWESOME TEXT GOES HERE</div><div class="sub">Sub title goes here</div><div class="rule"></div>
  <div class="logo"><i></i>BRIGHTVALE</div>
  <div class="stat" style="left:28px;top:50px;width:136px;height:62px"><p>Lorem ipsum is simply dummy text of the printing and typesetting industry.</p><b>310</b></div>
  <div class="stat mid" style="left:190px;top:50px;width:136px;height:62px"><p>Lorem ipsum is simply dummy text of the printing and typesetting industry.</p><b>150</b></div>
  <div class="stat" style="left:350px;top:50px;width:136px;height:62px"><p>Lorem ipsum is simply dummy text of the printing and typesetting industry.</p><b>9.010</b></div>
  <svg class="svgabs" width="516" height="290">
    <g font-family="Open Sans" font-size="4.5" fill="#3a4556">
      <text x="28" y="160">7</text><text x="28" y="171">6</text><text x="28" y="182">5</text><text x="28" y="193">4</text><text x="28" y="204">3</text><text x="28" y="215">2</text><text x="28" y="226">1</text><text x="28" y="237">0</text>
      <g text-anchor="middle"><text x="56" y="252">Day 1</text><text x="94" y="252">Day 2</text><text x="132" y="252">Day 3</text><text x="170" y="252">Day 4</text><text x="208" y="252">Day 5</text><text x="246" y="252">Day 6</text><text x="284" y="252">Day 7</text><text x="322" y="252">Day 8</text><text x="360" y="252">Day 9</text><text x="398" y="252">Day 10</text><text x="436" y="252">Day 11</text><text x="474" y="252">Day 12</text></g>
    </g>
    <path d="M56 212 C110 200 150 214 200 200 S240 180 280 188 S360 176 400 190 S460 196 476 192" fill="none" stroke="#9dbde6" stroke-width="1.2"/>
    <path d="M56 218 C110 206 150 210 200 196 S240 184 280 192 S360 186 400 196 S460 198 476 196" fill="none" stroke="#2b7fd6" stroke-width="1.6"/>
    <path d="M56 222 C110 214 150 206 200 200 S240 190 280 196 S360 194 400 202 S460 204 476 200" fill="none" stroke="#1d3c86" stroke-width="1"/>
    <line x1="226" y1="176" x2="226" y2="190" stroke="#1d3c86" stroke-width=".6"/>
    <circle cx="226" cy="190" r="2.6" fill="#fff" stroke="#1d3c86" stroke-width="1.2"/>
    <rect x="212" y="164" width="28" height="12" rx="2" fill="#2b7fd6"/>
    <text x="226" y="172" font-family="Open Sans" font-size="4.5" fill="#fff" text-anchor="middle">489.12</text>
  </svg>
  <div class="ft"><div class="n">18</div><div class="c">STRICTLY CONFIDENTIAL</div><div class="l">[Company logo]</div></div>
</section>

<!-- Slide break -->
<section class="slide big" style="left:493px;top:995px;background:linear-gradient(135deg,#2471c9,#1d4a9b)">
  <div class="abs" style="left:16px;top:74px;font:800 40px/1 'Montserrat',sans-serif;color:rgba(255,255,255,.14)">01</div>
  <div class="abs" style="left:30px;top:90px;font:700 32px/.95 'Open Sans',sans-serif;color:#fff">Slide<br>Break</div>
  <div class="abs" style="left:30px;top:178px;width:330px;font:400 5px/1.4 'Open Sans',sans-serif;color:#fff">Lorem ipsum dolor sit amet, consectetur adipiscing elit, sed do eiusmod tempor incididunt ut labore et dolore magna aliqua. Lorem ipsum dolor sit amet, consectetur adipiscing elit, sed do eiusmod tempor incididunt ut labore et dolore magna aliqua. Ut enim ad minim veniam, quis nostrud exercitation ullamco laboris nisi ut aliquip.</div>
</section>

</body>
</html>
```